Redesign Colorful Business Card

Please redesign the card attached. It is too busy. Please don't eliminate any of the words. The repetivite word "free" can be used less often.

Target Market(s)

College Students.

Contact Information for Business Card

The details listed in the attached image

Font styles to use
Sans Serif

Requirements
Must have
• A clear and simple presentation and must be attractive.

```html
<!DOCTYPE html>
<html lang="en">
<head>
<meta charset="utf-8">
<title>StudyBrisk Business Card</title>
<link rel="stylesheet" href="https://fonts.googleapis.com/css2?family=Jost:wght@400;500&display=swap">
<style>
  :root {
    --page-bg: #6f7073;
    --card-dark: #07080d;
    --card-navy: #1b2240;
    --card-sheen: #4a5680;
    --badge-red: #d9262a;
    --white: #ffffff;
    --tone-cyan: #7cc9dc;
    --tone-cream: #f2e49a;
    --tone-green: #6db33f;
  }
  * { margin: 0; padding: 0; box-sizing: border-box; }
  html, body {
    width: 1200px;
    height: 900px;
    overflow: hidden;
    background: var(--page-bg);
    font-family: "Jost", sans-serif;
  }
  .business-card {
    position: absolute;
    left: 50px;
    top: 136px;
    width: 1100px;
    height: 628px;
    border-radius: 44px;
    overflow: hidden;
    background:
      linear-gradient(155deg, transparent 38%, rgba(74,86,128,0.45) 44%, transparent 50%),
      linear-gradient(155deg, transparent 55%, rgba(74,86,128,0.35) 60%, transparent 66%),
      linear-gradient(155deg, transparent 18%, rgba(74,86,128,0.3) 24%, transparent 30%),
      linear-gradient(155deg, transparent 72%, rgba(74,86,128,0.4) 78%, transparent 84%),
      linear-gradient(120deg, var(--card-dark) 0%, var(--card-navy) 55%, var(--card-dark) 100%);
  }
  .mascot-art {
    position: absolute;
    left: 68px;
    top: 62px;
    width: 434px;
    height: 463px;
  }
  .brand-name {
    position: absolute;
    left: 50px;
    top: 536px;
    font-size: 50px;
    font-weight: 400;
    color: var(--white);
    letter-spacing: 0.5px;
    line-height: 1;
  }
  .benefit {
    position: absolute;
    left: 559px;
    display: flex;
    gap: 26px;
  }
  .benefit--time { top: 62px; }
  .benefit--class { top: 256px; }
  .benefit--memory { top: 450px; }
  .free-badge {
    position: relative;
    width: 79px;
    height: 43px;
    margin-top: 0;
    background: var(--badge-red);
    border-radius: 10px;
    color: var(--white);
    font-size: 25px;
    font-weight: 500;
    line-height: 43px;
    text-align: center;
    flex-shrink: 0;
  }
  .free-badge::after {
    content: "";
    position: absolute;
    left: 16px;
    bottom: -10px;
    border-left: 4px solid transparent;
    border-right: 6px solid transparent;
    border-top: 11px solid var(--badge-red);
  }
  .benefit-text {
    font-size: 39px;
    font-weight: 400;
    line-height: 43px;
    text-transform: uppercase;
    letter-spacing: 0.5px;
    margin-top: -2px;
  }
  .benefit--time .benefit-text { color: var(--tone-cyan); }
  .benefit--class .benefit-text { color: var(--tone-cream); }
  .benefit--memory .benefit-text { color: var(--tone-green); }
</style>
</head>
<body>
  <main class="business-card">
    <svg class="mascot-art" viewBox="0 0 434 463" role="img" aria-label="Brand mascot illustration in multicoloured vertical stripes">
      <defs>
        <linearGradient id="mascotTone" x1="0" y1="0" x2="1" y2="0">
          <stop offset="0" stop-color="#3d5a8a" stop-opacity="0.55"/>
          <stop offset="0.5" stop-color="#7a4a78" stop-opacity="0.55"/>
          <stop offset="1" stop-color="#8a6a3a" stop-opacity="0.55"/>
        </linearGradient>
      </defs>
      <rect x="0" y="0" width="434" height="463" rx="24" fill="url(#mascotTone)"/>
    </svg>

    <p class="brand-name">StudyBrisk.com</p>

    <section class="benefit benefit--time">
      <span class="free-badge">FREE</span>
      <p class="benefit-text">Cut study time<br>down by<br>upto 50%</p>
    </section>

    <section class="benefit benefit--class">
      <span class="free-badge">FREE</span>
      <p class="benefit-text">Learn a subject<br>without having to<br>go to class</p>
    </section>

    <section class="benefit benefit--memory">
      <span class="free-badge">FREE</span>
      <p class="benefit-text">Memorize<br>anythig<br>quickly</p>
    </section>
  </main>
</body>
</html>
```